Fotograf sucht Gutschein-Design
Schnell, unkomplizierte Abwicklung und ich habe ein wunderschönes Design erhalten.
Zielgruppe
Bin Fotograf spezialisiert auf Pärchen und Hochzeitsfotos
Aufgabenstellung
Möchte einen neuen Gutschein für meine Zwecke haben. Sollte zu meinem fotografischen Stil passen, hell/ freundlich/ Retro? Vintage? Kann auch gerne 'Verzierung' mit Blümchen/ Zweige enthalten wenns passt. am besten ein wenig auf meiner Homepage orientieren >>> www.tobiasrandecker.com - Auch meine Logo/ Firmendaten sollten wo passend platziert sein. Mein Logo/ und Fotos füge ich bei und können wie es gut passt verwendet werden. Das auf dem Einzelbild bin ich, falls es wo passt wäre es toll. Schriftmäßig sollte es natürlich irgendwie das Wort Gutschein enthalten. Dann noch 'von' und 'für' und ein Feld wo ich händisch die Gutscheinnummer eintragen kann. Das Format/ Form überlasse ich auch ganz euch aber werde voraussichtlich bei karteneck bestellen. (Falls es um das finden des passenden Formats/ Form geht). Bei Fragen könnt ihr euch gerne jederzeit melden.

```html
<!DOCTYPE html>
<html lang="de">
<head>
<meta charset="utf-8">
<title>Gutschein – Tobias Randecker Fotografie</title>
<link rel="stylesheet" href="https://fonts.googleapis.com/css2?family=Sacramento&family=Jost:wght@400&family=Antonio:wght@400&display=swap">
<style>
  :root {
    --paper: #ffffff;
    --panel: #efefef;
    --ink: #111111;
    --frame: #222222;
  }
  * { margin: 0; padding: 0; box-sizing: border-box; }
  html, body { width: 1200px; height: 846px; overflow: hidden; background: var(--paper); }
  .voucher {
    position: relative; width: 1200px; height: 846px;
    background: var(--paper); border: 1px solid var(--frame);
  }
  .voucher__panel {
    position: absolute; left: 30px; top: 30px; width: 1140px; height: 787px;
    background: var(--panel);
  }
  .photo { position: absolute; }
  .photo--portrait { left: 46px; top: 40px; width: 243px; height: 337px;
    background: linear-gradient(160deg, #c9cfd3 0%, #8a7d63 45%, #6f6a5e 70%, #b5652f 100%); }
  .photo--walk { left: 300px; top: 38px; width: 282px; height: 187px;
    background: linear-gradient(180deg, #a9b7bb 0%, #5e7a4c 35%, #c8c2b4 70%, #d8d2c6 100%); }
  .photo--meadow { left: 591px; top: 36px; width: 282px; height: 187px;
    background: linear-gradient(90deg, #4f7a3a 0%, #88a86a 45%, #b9c89c 65%, #5b8042 100%); }
  .photo--rocks { left: 882px; top: 38px; width: 282px; height: 186px;
    background: linear-gradient(180deg, #aebcc4 0%, #8a9b72 30%, #c9c3b6 60%, #b9b1a2 100%); }
  .photo--boat { left: 882px; top: 233px; width: 282px; height: 186px;
    background: linear-gradient(135deg, #cdb9a5 0%, #6d7f8c 40%, #e3e5e8 70%, #b8a898 100%); }
  .photo--shore { left: 882px; top: 427px; width: 282px; height: 186px;
    background: linear-gradient(160deg, #9aa6a8 0%, #b8ab96 40%, #7d7a66 70%, #a79b88 100%); }
  .photo--beach { left: 882px; top: 622px; width: 282px; height: 187px;
    background: linear-gradient(180deg, #d8d1c8 0%, #c4b6a8 50%, #6a6b70 80%, #8fb2c6 100%); }

  .amount {
    position: absolute; left: 509px; top: 348px; width: 317px; height: 58px;
    border-bottom: 3px solid var(--ink);
    font-family: "Jost", sans-serif; font-size: 50px; line-height: 58px; color: var(--ink);
  }
  .title {
    position: absolute; left: 50px; top: 392px;
    font-family: "Sacramento", cursive; font-weight: 400; font-size: 200px; line-height: 200px;
    color: var(--ink); white-space: nowrap;
  }
  .fields { position: absolute; left: 76px; top: 676px; font-family: "Jost", sans-serif; font-size: 19px; color: var(--ink); }
  .field { display: flex; align-items: flex-end; height: 30px; }
  .field__label { width: 58px; }
  .field__line { width: 177px; border-bottom: 1.5px solid var(--ink); height: 20px; }
  .field--number { margin-top: 22px; }
  .field--number .field__label { width: auto; margin-right: 4px; }
  .brand {
    position: absolute; left: 690px; top: 700px; width: 380px;
    color: var(--ink); text-align: center;
  }
  .brand__name {
    font-family: "Antonio", sans-serif; font-weight: 400;
    font-size: 34px; letter-spacing: 9px; padding-left: 9px; line-height: 1.1;
  }
  .brand__line {
    font-family: "Jost", sans-serif; font-weight: 400;
    font-size: 21px; letter-spacing: 10px; padding-left: 10px; margin-top: 12px;
  }
</style>
</head>
<body>
<main class="voucher">
  <div class="voucher__panel"></div>
  <div class="photo photo--portrait" role="img" aria-label="Porträt des Fotografen, sitzend auf einem Felsen neben einem Baum"></div>
  <div class="photo photo--walk" role="img" aria-label="Paar geht Hand in Hand an der Küste"></div>
  <div class="photo photo--meadow" role="img" aria-label="Paar umarmt sich im hohen Gras"></div>
  <div class="photo photo--rocks" role="img" aria-label="Paar sitzt auf Felsen am Meer"></div>
  <div class="photo photo--boat" role="img" aria-label="Paar kuschelt in einem alten Holzboot"></div>
  <div class="photo photo--shore" role="img" aria-label="Paar sitzt am steinigen Ufer"></div>
  <div class="photo photo--beach" role="img" aria-label="Babybauch-Shooting eines Paares am Strand"></div>

  <div class="amount">€</div>
  <h1 class="title">Gutschein</h1>

  <div class="fields">
    <div class="field"><span class="field__label">von:</span><span class="field__line"></span></div>
    <div class="field"><span class="field__label">für:</span><span class="field__line"></span></div>
    <div class="field field--number"><span class="field__label">Gutscheinnummer:</span><span class="field__line"></span></div>
  </div>

  <div class="brand">
    <div class="brand__name">TOBIAS RANDECKER</div>
    <div class="brand__line">FOTOGRAFIE</div>
  </div>
</main>
</body>
</html>
```